Website/Logo Design

We need a logo and website design for an opinion mining startup called VantroLux. Our technology mines the web to automatically discover what people are saying about brands, products, etc. The project we are fielding here is for our informational, public-facing website. In its initial incarnation, it will simply be a vehicle for marketing materials and information on our company and its offerings, but it should be flexible enough to expand as more content/functionality is added.

Some designs we like are:
http://www.brivel-nodo.com
http://www.tarnwisp.com
http://www.kvh.com
http://www.zellmorit.com
http://quontavel.com
http://marbiquex.com
http://www.vadup.com
Updates

All, please try to shy away from using a photo of a person as the focal point of the design.  Our company is more technological than social.

Target Market(s)

Primarily businesses interested in sentiment analysis (typically companies involved in advertising, market research, PR, etc.)

Industry/Entity Type

It Company

Requirements
Must have
• We are looking for a clean, modern, and professional design. This includes a logo, homepage, and internal page if it will differ from the homepage.
Nice to have
• It would be excellent if you could provide an HTML mockup if your design is chosen.
Should not have
• Flash, excessive bells and whistles

```html
<!DOCTYPE html>
<html lang="en">
<head>
<meta charset="utf-8">
<title>VantroLux – About</title>
<link href="https://fonts.googleapis.com/css2?family=Noto+Sans:wght@400;700&display=swap" rel="stylesheet">
<style>
:root{
  --page:#e6e6ea;
  --page-light:#f7f7f9;
  --purple:#5a428a;
  --purple-light:#7659a8;
  --purple-dark:#3f2c66;
  --link:#6a3fa8;
  --heading:#333338;
  --body:#8b8b90;
  --pill:#a9a9ad;
  --bar:#9c9ca0;
  --white:#ffffff;
  --tick:#d66fb4;
  --gold:#e8c24e;
  --rss:#e98a2c;
  --social:#8f8f93;
}
*{box-sizing:border-box;margin:0;padding:0}
html,body{width:1099px;height:1200px;overflow:hidden}
body{
  position:relative;
  font-family:"Noto Sans",sans-serif;
  color:var(--body);
  background:
    radial-gradient(ellipse 520px 300px at 200px 110px,var(--page-light),transparent 70%),
    radial-gradient(ellipse 600px 500px at 550px 600px,#efeff2,transparent 75%),
    linear-gradient(#d3d3d7 0,var(--page) 260px,var(--page) 100%);
}
.site-logo{position:absolute;left:80px;top:82px;display:flex;align-items:center;gap:10px}
.site-logo__name{font-size:46px;color:var(--purple);letter-spacing:-1px;line-height:1}
.site-logo__mark{width:52px;height:52px;background:var(--purple-light);border-radius:8px}

.main-nav{position:absolute;top:108px;left:473px;display:flex;gap:20px}
.main-nav a{
  display:block;height:26px;line-height:26px;padding:0 14px;border-radius:13px;
  background:var(--pill);color:var(--white);font-size:14.5px;text-decoration:none;
  box-shadow:0 4px 8px rgba(0,0,0,.12);
}
.main-nav a.is-active{background:var(--purple-dark)}

.page-banner{position:absolute;left:35px;top:174px;width:1036px;height:171px;border-radius:9px;overflow:hidden;background:var(--white)}
.page-banner__visual{position:absolute;right:0;top:0;width:418px;height:118px;
  background:linear-gradient(90deg,#ffffff 0%,#d9d2c7 25%,#6d5a4c 55%,#b49a86 75%,#7aa53a 100%)}
.page-banner__band{position:absolute;left:0;top:118px;width:100%;height:53px;
  background:linear-gradient(90deg,#4a3577,var(--purple) 50%,#4c3778)}
.page-banner__title{position:absolute;left:44px;top:132px;color:var(--white);font-size:21px;font-weight:400}

.content{position:absolute;left:76px;top:386px;width:680px}
.content h2{font-size:14.5px;font-weight:400;color:var(--heading);margin-bottom:20px}
.content p{font-size:14.2px;line-height:21.2px;margin-bottom:42px}
.feature-list{list-style:none;margin:-8px 0 42px 56px}
.feature-list li{position:relative;padding-left:29px;color:var(--link);font-size:14.5px;line-height:26px}
.feature-list svg{position:absolute;left:0;top:7px}

.contact-card{position:absolute;left:845px;top:768px;width:214px;height:209px;border-radius:8px;
  background:linear-gradient(180deg,#f6f6f8,rgba(240,240,243,.2));text-align:right;padding:0 20px 0 0;font-size:13px;line-height:21px}
.contact-card__title{position:absolute;left:33px;top:20px;color:var(--heading);font-size:14.5px;letter-spacing:.3px}
.contact-card__icon{position:absolute;right:16px;top:-6px}
.contact-card__rule{position:absolute;left:0;top:55px;width:100%;height:1px;background:linear-gradient(90deg,transparent,#dcdce0)}
.contact-card address{font-style:normal;position:absolute;right:20px;top:76px}
.contact-card strong{color:#66666b;font-weight:400}
.contact-card a{color:var(--link);text-decoration:none}

.clients-bar{position:absolute;left:35px;top:1027px;width:1036px;height:93px;border-radius:9px;
  background:linear-gradient(180deg,#a6a6aa,var(--bar));box-shadow:0 10px 16px rgba(0,0,0,.08)}
.clients-bar__label{position:absolute;left:44px;top:36px;color:var(--white);font-size:16px}
.client{position:absolute;top:34px;font-size:19px;color:#c4c4c8;transform:translateX(-50%);white-space:nowrap}
.client.is-hover{color:var(--white)}

.site-footer{position:absolute;top:1143px;left:76px;width:960px;font-size:12px}
.site-footer a{color:var(--link);text-decoration:none}
.site-footer__legal{position:absolute;left:221px;top:0}
.site-footer__follow{position:absolute;left:785px;top:0;display:flex;align-items:center;gap:10px}
.social-icon{display:inline-block;width:19px;height:19px;border-radius:3px;background:var(--social)}
.social-icon--feed{background:var(--rss)}
</style>
</head>
<body>

<header>
  <div class="site-logo"><span class="site-logo__name">VantroLux</span><span class="site-logo__mark"></span></div>
  <nav class="main-nav">
    <a href="#">About VantroLux</a>
    <a href="#">How We Work</a>
    <a href="#" class="is-active">Case Studies</a>
    <a href="#">Pricing</a>
    <a href="#">Contact</a>
  </nav>
</header>

<section class="page-banner">
  <div class="page-banner__visual" role="img" aria-label="Photo of three colleagues looking at a screen together"></div>
  <div class="page-banner__band"></div>
  <h1 class="page-banner__title">About VantroLux</h1>
</section>

<main class="content">
  <h2>What We Do</h2>
  <p>Sed ultricies enim sit amet arcu pellentesque congue sit amet in neque. Quisque vel nunc eget magna blandit pellentesque. Integer eget risus eget mi facilisis cursus. Curabitur eleifend hendrerit pharetra. Sed scelerisque, eros eu feugiat mattis, tellus lacus varius lectus, eget pretium arcu erat sit amet magna. Donec non malesuada ante. Phasellus vitae ante mauris. Donec mattis ipsum risus. Pellentesque ut sapien ante, at ornare mi. Sed hendrerit, sapien id lacinia tristique, justo nisi viverra tellus, et pharetra ipsum felis non velit.</p>

  <h2>Our Mission</h2>
  <p>Vivamus lorem metus, auctor a lobortis quis, pretium in nisi. Curabitur magna quam, semper non accumsan ut, placerat ut diam. In volutpat elementum eros vitae mattis. Aenean iaculis felis quis arcu tincidunt id aliquam lacus blandit.</p>
  <ul class="feature-list">
    <li><svg width="15" height="12" viewBox="0 0 15 12"><path d="M1 6l4 4 9-9" fill="none" stroke="var(--tick)" stroke-width="2.4"/></svg>Nullam dictum, nisi ut aliquam aliquam</li>
    <li><svg width="15" height="12" viewBox="0 0 15 12"><path d="M1 6l4 4 9-9" fill="none" stroke="var(--tick)" stroke-width="2.4"/></svg>Urna dolor dictum turpis, at luctus nisi nibh</li>
    <li><svg width="15" height="12" viewBox="0 0 15 12"><path d="M1 6l4 4 9-9" fill="none" stroke="var(--tick)" stroke-width="2.4"/></svg>Vel elit. Mauris eget neque tortor, quis iaculis odio.</li>
  </ul>

  <h2>Investor Relations</h2>
  <p>Etiam ac dui est, dapibus sagittis felis. Sed luctus, ipsum ut mollis egestas, eros lorem commodo nibh, sodales facilisis nisi tellus et enim. Mauris eu rhoncus risus. Aenean id diam sit amet sem bibendum malesuada a ac tortor. Nam venenatis mattis porta. Cras ipsum velit, porttitor quis condimentum ut, vestibulum et mi.</p>
</main>

<aside class="contact-card">
  <span class="contact-card__title">CONTACT US</span>
  <svg class="contact-card__icon" width="50" height="48" viewBox="0 0 50 48">
    <g transform="rotate(-18 25 24)">
      <rect x="4" y="10" width="42" height="28" rx="2" fill="var(--gold)"/>
      <path d="M4 12l21 15 21-15" fill="none" stroke="#c49a28" stroke-width="1.5"/>
    </g>
  </svg>
  <div class="contact-card__rule"></div>
  <address>
    <strong>VantroLux Ltd.</strong><br>
    42 Harrow Lane<br>
    HLB 4R2, Leeds, UK<br><br>
    Tel:&nbsp;&nbsp; 0044-210-55472<br>
    E-mail:&nbsp;&nbsp; <a href="#">info@vantrolux.com</a>
  </address>
</aside>

<section class="clients-bar">
  <span class="clients-bar__label">Some of our clients...</span>
  <span class="client" style="left:314px">Korvane</span>
  <span class="client" style="left:444px">Lumetra</span>
  <span class="client" style="left:572px">Ostrel</span>
  <span class="client" style="left:703px">Pelvora</span>
  <span class="client is-hover" style="left:831px">Quindo</span>
  <span class="client" style="left:962px">Sarvix</span>
</section>

<footer class="site-footer">
  <span>Copyright 2010, VantroLux Ltd.</span>
  <span class="site-footer__legal"><a href="#">Terms of Use</a> &nbsp;/&nbsp; <a href="#">Contact</a></span>
  <span class="site-footer__follow">Follow us via
    <span class="social-icon"></span>
    <span class="social-icon"></span>
    <span class="social-icon social-icon--feed"></span>
  </span>
</footer>

</body>
</html>
```